Denture Clinic needs a newspaper advertisement

We need a revamped newspaper advertisement for our denture clinic based in Tweed Heads, Australia. We are currently promoting a new product called FlexaVire which is a virtually non breakable, flexible denture. We have an ad the newspaper designed themselves but I feel the ad gets lost on the page and isn't effective. They have used our brand colours but apparently so does everyone else in the newspaper! We would like to see an ad that shows a quality, state of the art product but something that jumps out of the page and overrides the other ads nearby. We can't use colours that stimulate fear (like blood red) or anxiety being a dentist or black.

I have also attached a copy of the one-off full page ad we ran which shows more information about the product.

The ad size is 92mm high by 129mm wide.

Target Market(s)

95% of our patients are 65+ years old

Industry/Entity Type

Clinic

Requirements
Must have
• Must show the denture, our name, logo and details and state it is virtually unbreakable and flexible.
Should not have
• Colours that evoke fear, anxiety, trepidation.

```html
<!DOCTYPE html>
<html lang="en">
<head>
<meta charset="utf-8">
<title>Riverbend Denture Clinic – FlexaVire Flexible Dentures</title>
<link rel="stylesheet" href="https://fonts.googleapis.com/css2?family=Jost:wght@400;500;600&display=swap">
<style>
  :root {
    --pink: #c04770;
    --white: #ffffff;
    --badge-blue: #1b6c9e;
    --link-blue: #1a5d8c;
    --ink: #2b2b2b;
    --photo-light: #e6dccf;
    --photo-mid: #b9ab9c;
    --photo-dark: #8f8a86;
  }
  * { box-sizing: border-box; margin: 0; padding: 0; }
  html, body { width: 1200px; height: 856px; overflow: hidden; background: var(--white); }
  body { font-family: "Jost", "Futura", sans-serif; color: var(--white); }
  .ad { position: relative; width: 1200px; height: 856px; overflow: hidden; }
  .ad-backdrop { position: absolute; left: 0; top: 0; width: 1200px; height: 708px; }
  .couple-photo {
    position: absolute; left: 670px; top: 0; width: 530px; height: 468px;
    border-bottom-left-radius: 36px;
    background: linear-gradient(120deg, var(--photo-light) 0%, var(--photo-mid) 55%, var(--photo-dark) 100%);
  }
  .allergy-badge {
    position: absolute; left: 698px; top: 14px; width: 212px; height: 212px;
    border-radius: 50%; background: var(--badge-blue);
    display: flex; align-items: center; justify-content: center;
  }
  .allergy-badge p {
    transform: rotate(-22deg); text-align: center; font-weight: 600;
    font-size: 21px; line-height: 1.08; letter-spacing: 0.3px; text-transform: uppercase;
  }
  .headline {
    position: absolute; left: 36px; top: 30px; width: 630px;
    font-weight: 400; font-size: 63px; line-height: 78px; letter-spacing: 0.5px;
    text-transform: uppercase;
  }
  .product-card {
    position: absolute; left: 36px; top: 322px; width: 594px; height: 344px;
    background: var(--white); border-radius: 0 28px 28px 0; color: var(--ink);
  }
  .product-intro {
    position: absolute; left: 28px; top: 24px; width: 440px; z-index: 1;
    font-size: 31px; line-height: 37px; font-weight: 400; color: #222;
  }
  .product-note {
    position: absolute; left: 28px; top: 264px; width: 270px; z-index: 1;
    font-size: 16.5px; line-height: 20px; color: #333;
  }
  .denture-photo {
    position: absolute; left: 300px; top: 40px; width: 282px; height: 294px;
    clip-path: polygon(188px 0, 282px 0, 282px 294px, 0 294px, 0 176px, 188px 176px);
    background: radial-gradient(ellipse at 60% 65%, #f1e6e2 0%, #e2a6a6 40%, #c9787d 70%, #d9a0a3 100%);
  }
  .call-to-action {
    position: absolute; left: 660px; top: 508px; width: 540px; text-align: center;
    font-weight: 600; font-size: 34px; line-height: 46px; text-transform: uppercase;
  }
  .phone-number {
    position: absolute; left: 660px; top: 604px; width: 540px; text-align: center;
    font-weight: 500; font-size: 62px; line-height: 70px; letter-spacing: 1px;
  }
  .contact-web {
    position: absolute; left: 29px; top: 744px;
    font-weight: 600; font-size: 27px; color: var(--link-blue);
  }
  .contact-address {
    position: absolute; left: 29px; top: 790px;
    font-size: 23.5px; color: var(--ink);
  }
  .clinic-name {
    position: absolute; left: 828px; top: 740px; width: 360px; height: 92px;
    display: flex; align-items: center; gap: 14px;
    font-weight: 600; font-size: 29px; line-height: 32px; color: var(--link-blue);
  }
  .clinic-name .mark { width: 58px; height: 58px; border-radius: 50%; background: var(--link-blue); flex: none; }
</style>
</head>
<body>
<main class="ad">
  <svg class="ad-backdrop" viewBox="0 0 1200 708" aria-hidden="true">
    <path d="M0 0 H634 A36 36 0 0 1 670 36 V420 H1200 V708 H0 Z" fill="var(--pink)"/>
  </svg>

  <div class="couple-photo" role="img" aria-label="Photo of a smiling senior couple leaning close together"></div>

  <div class="allergy-badge"><p>Suitable for<br>patients with<br>allergic<br>reactions!</p></div>

  <h1 class="headline">Want virtually*<br>unbreakable,<br>flexible dentures?</h1>

  <section class="product-card">
    <div class="denture-photo" role="img" aria-label="Photo of a flexible partial denture with a translucent pink base"></div>
    <p class="product-intro">Introducing the FlexaVire<br>denture injection system<br>by Corvana, using advanced<br>dental prosthetic<br>technology.</p>
    <p class="product-note">*Virtually unbreakable refers to<br>&nbsp;the base of the denture only.</p>
  </section>

  <p class="call-to-action">Call to find something<br>to smile about!</p>
  <p class="phone-number">(07) 5500 1987</p>

  <p class="contact-web">www.riverbenddentureclinic.com.au</p>
  <p class="contact-address">Daniel Keswick AdvDipDP Dip DT - 12 Harbour Lane, Tweed Heads</p>

  <div class="clinic-name"><span class="mark"></span><span>Riverbend<br>Denture Clinic</span></div>
</main>
</body>
</html>
```